Vr holdings enterprise pty ltd

2 sided card black and red with white
Very professional and elegant

Target Market(s)

Construction and Development

Industry/Entity Type

Construction and development

Contact Information for Business Card

One side black, one side red/or white business logo in top corner, email: morgan@vrholdingsgroup.example

Requirements
Should not have
• Blue

```html
<!DOCTYPE html>
<html lang="en">
<head>
<meta charset="utf-8">
<title>VR Holdings – Business Card</title>
<link rel="stylesheet" href="https://fonts.googleapis.com/css2?family=Poppins:wght@300;400;600&display=swap">
<style>
  :root{
    --backdrop:#d9d9d9;
    --card-red:#e63012;
    --card-black:#161616;
    --ink-white:#ffffff;
    --accent-red:#e63012;
  }
  *{box-sizing:border-box;margin:0;padding:0}
  html,body{width:1200px;height:800px;overflow:hidden}
  body{
    background:var(--backdrop);
    font-family:"Poppins",sans-serif;
    display:flex;align-items:center;justify-content:center;gap:40px;
  }
  .card{
    position:relative;width:540px;height:309px;border-radius:22px;
    color:var(--ink-white);overflow:hidden;
  }
  .card--front{background:var(--card-red)}
  .card--back{background:var(--card-black)}

  .brand{
    display:flex;align-items:center;gap:8px;
    font-weight:600;text-transform:uppercase;letter-spacing:3px;
    color:var(--ink-white);white-space:nowrap;
  }
  .brand__dot{width:8px;height:8px;border-radius:50%;background:var(--ink-white)}
  .card--back .brand__dot{background:var(--accent-red)}

  .card--front .brand{position:absolute;top:62px;left:0;right:0;justify-content:center;font-size:26px}
  .card--back .brand{position:absolute;top:50%;left:0;right:0;transform:translateY(-50%);justify-content:center;font-size:38px}

  .divider{position:absolute;left:28px;right:28px;top:180px;height:1px;background:var(--ink-white);opacity:.85}

  .holder{position:absolute;left:30px;top:145px;font-size:21px;font-weight:400;letter-spacing:1.5px;text-transform:uppercase}

  .contact{position:absolute;left:30px;top:192px;list-style:none;font-size:12.5px;font-weight:300;line-height:19px}
  .contact li{display:flex;align-items:center;gap:8px}
  .contact svg{width:11px;height:11px;flex:none}

  .address{position:absolute;right:30px;top:192px;text-align:right;font-size:12.5px;font-weight:300;line-height:19px}
</style>
</head>
<body>
  <section class="card card--front" aria-label="Business card, contact side">
    <div class="brand"><span>VR Holdings</span><span class="brand__dot"></span></div>
    <p class="holder">Morgan</p>
    <div class="divider"></div>
    <ul class="contact">
      <li>
        <svg viewBox="0 0 12 12" aria-hidden="true"><path d="M2.5 1h2l1 3-1.3 1a7 7 0 0 0 2.8 2.8l1-1.3 3 1v2a1 1 0 0 1-1 1A10 10 0 0 1 1.5 2a1 1 0 0 1 1-1z" fill="#fff"/></svg>
        555-214-0386
      </li>
      <li>
        <svg viewBox="0 0 12 12" aria-hidden="true"><rect x="3" y="0.8" width="6" height="10.4" rx="1" fill="none" stroke="#fff" stroke-width="1.2"/></svg>
        555-781-2290
      </li>
      <li>
        <svg viewBox="0 0 12 12" aria-hidden="true"><rect x="0.8" y="2.5" width="10.4" height="7" fill="none" stroke="#fff" stroke-width="1.2"/><path d="M1 3l5 3.5L11 3" fill="none" stroke="#fff" stroke-width="1.2"/></svg>
        morgan@vrholdingsgroup.example
      </li>
    </ul>
    <address class="address" style="font-style:normal">
      42 Alder Ridge Road<br>
      Juniper Falls, Yukon 20481<br>
      www.vrholdingsgroup.example
    </address>
  </section>

  <section class="card card--back" aria-label="Business card, brand side">
    <div class="brand"><span>VR Holdings</span><span class="brand__dot"></span></div>
  </section>
</body>
</html>
```